Real Estate Flyer

Hi - I am assisting a relative to sell a unit. I am looking to have a two page flyer designed (configured as a single page with back to back printing). I have uploaded two samples to give you an idea of the look and feel - one which relates to this property when originally purchased, the other for a different property.
The flyer should includes several key photos on the front along with the wording. The rear should include any secondary photos along with the floor plan.
The flyer should be close to A4 size.

Updates
Hi,
Industry/Entity Type
Real Estate
Look and feel
Each slider illustrates characteristics of the customer's brand and the style your logo design should communicate.

```html
<!DOCTYPE html>
<html lang="en">
<head>
<meta charset="utf-8">
<title>12/40-48 Linden Street, Harbour Heights – Private Sale Flyer</title>
<link rel="stylesheet" href="https://fonts.googleapis.com/css2?family=Arimo:wght@400;700&display=swap">
<style>
:root{
  --olive:#7b7930;
  --olive-text:#7a7530;
  --heading:#6e6c45;
  --body:#6d6d6d;
  --accent:#e0195b;
  --paper:#ffffff;
  --line:#222;
}
*{margin:0;padding:0;box-sizing:border-box}
html,body{width:1200px;height:832px;overflow:hidden;background:var(--paper)}
body{font-family:"Arimo",Arial,sans-serif;position:relative}
.abs{position:absolute}
.photo-set{left:0;top:0}
.stats{display:flex;align-items:center;gap:6px;color:var(--olive);font-weight:700}
.stats .num{font-size:36px;line-height:1}
.stats svg{display:block}
.stats-front{left:334px;top:412px}
.stats-back{left:1022px;top:62px;flex-direction:column;align-items:flex-start;gap:4px}
.stats-back .row{display:flex;align-items:center;gap:4px}
.address{left:262px;top:460px;color:var(--accent);font-weight:700;text-align:center;width:296px}
.address .street{font-size:22px;display:block}
.address .suburb{font-size:26px;display:block;margin-top:4px}
.headline{left:35px;top:500px;width:260px;color:var(--heading);font-size:19px;font-weight:700;line-height:1.2}
.intro{left:35px;top:553px;width:262px;color:var(--body);font-size:10.4px;line-height:1.28}
.rates{left:35px;top:656px;color:var(--body);font-size:10.4px;line-height:1.28}
.rates dt{float:left;width:88px}
.rates dd{margin-left:88px}
.rental{left:35px;top:707px;color:var(--body);font-size:15px;font-weight:700;line-height:1.3}
.features{left:305px;top:548px;width:265px;list-style:none;color:var(--olive-text);font-size:15px;line-height:1.32}
.features li{padding-left:10px;text-indent:-10px}
.features li::before{content:"• "}
.plan{left:612px;top:58px;width:228px;height:278px}
.carspace{left:948px;top:66px;width:52px;height:108px;border:1px solid var(--line)}
.plan-meta{left:915px;top:210px;width:218px;font-size:5.5px;color:#333}
.plan-meta .area{margin-bottom:16px}
.plan-meta .label{display:flex;justify-content:space-between;font-weight:700;font-size:6.5px;border-bottom:1px solid #333;padding-bottom:2px}
.plan-meta .disclaimer{font-size:3.6px;margin-top:3px;line-height:1.3}
.inspect{left:625px;top:613px;color:var(--body);font-size:17px;font-weight:700;line-height:1.3}
.contact{left:617px;top:668px;width:540px;height:114px;background:var(--olive);color:#fff;font-weight:700;text-align:center;padding-top:18px}
.contact .line1{font-size:29px}
.contact .line1 small{font-size:21px}
.contact .line2{font-size:29px;margin-top:6px}
.contact .line2 small{font-size:21px}
</style>
</head>
<body>

<svg class="abs photo-set" width="600" height="500" viewBox="0 0 600 500">
  <defs>
    <linearGradient id="pool" x1="0" y1="0" x2="0" y2="1">
      <stop offset="0" stop-color="#b8683f"/>
      <stop offset="0.55" stop-color="#a85a36"/>
      <stop offset="0.7" stop-color="#4fb7cf"/>
      <stop offset="1" stop-color="#2a8fb0"/>
    </linearGradient>
    <linearGradient id="terrace" x1="0" y1="0" x2="1" y2="1">
      <stop offset="0" stop-color="#d2b79c"/>
      <stop offset="0.5" stop-color="#c8915f"/>
      <stop offset="1" stop-color="#e0c6a8"/>
    </linearGradient>
  </defs>
  <rect x="330" y="28" width="242" height="367" fill="url(#pool)" role="img" aria-label="Photo of the building tower and outdoor pool"/>
  <path d="M18 28 H300 Q420 250 255 480 H18 Z" fill="url(#terrace)" stroke="#fff" stroke-width="8" role="img" aria-label="Photo of the curved full-width terrace"/>
</svg>

<div class="abs stats stats-front">
  <span class="num">2</span>
  <svg width="36" height="36" viewBox="0 0 36 36"><circle cx="18" cy="18" r="18" fill="currentColor"/><rect x="8" y="16" width="20" height="6" fill="#fff"/><rect x="8" y="12" width="3" height="14" fill="#fff"/><rect x="12" y="13" width="6" height="3" rx="1.5" fill="#fff"/></svg>
  <span class="num" style="margin-left:12px">1</span>
  <svg width="36" height="36" viewBox="0 0 36 36"><circle cx="18" cy="18" r="18" fill="currentColor"/><rect x="7" y="17" width="22" height="3" fill="#fff"/><path d="M9 20 H27 L25 26 H11 Z" fill="#fff"/><rect x="9" y="9" width="3" height="9" fill="#fff"/></svg>
  <span class="num" style="margin-left:12px">1</span>
  <svg width="36" height="36" viewBox="0 0 36 36"><circle cx="18" cy="18" r="18" fill="currentColor"/><path d="M9 21 L12 13 H24 L27 21 V26 H9 Z" fill="#fff"/><circle cx="13" cy="22" r="1.6" fill="currentColor"/><circle cx="23" cy="22" r="1.6" fill="currentColor"/></svg>
</div>

<h1 class="abs address"><span class="street">12/40-48 Linden Street,</span><span class="suburb">HARBOUR HEIGHTS</span></h1>

<h2 class="abs headline">Oversized apartment in a lifestyle location</h2>

<p class="abs intro">Peacefully positioned on the 5th floor of a refurbished security building, this superbly spacious residence combines modern, low maintenance apartment living with inviting prospects for the entertainer. Boasting a huge full-width terrace on-title, its sought-after setting in the heart of Harbour Heights offers the ultimate in lifestyle and convenience.</p>

<dl class="abs rates">
  <dt>Water Rates:</dt><dd>To be provided on finalizing design</dd>
  <dt>Council Rates:</dt><dd>&nbsp;&nbsp;To be provided on finalizing design</dd>
  <dt>Strata Rates:</dt><dd>To be provided on finalizing design</dd>
</dl>

<p class="abs rental">Estimated Market<br>Rental:&nbsp; $700.00 p/w<br>Inspect :&nbsp; Sat 10:45 – 11:30;<br>Wed 12:00 – 12:30</p>

<ul class="abs features">
  <li>Expansive open plan living and dining area</li>
  <li>Terrace features city and Harbour Bay glimpses</li>
  <li>Kitchen updated with Verano gas appliances</li>
  <li>Built-ins in both bedrooms, fully tiled bathrooms</li>
  <li>Internal laundry, secure parking, lift, outdoor pool and gymnasium</li>
  <li>Steps to station, Parkside Mall and Linden Park</li>
</ul>

<div class="abs plan" role="img" aria-label="Floor plan: main bed, bed 2, kitchen, living and dining, two curved balconies" style="background:#ececec;border:1px solid #bbb"></div>
<div class="abs carspace" role="img" aria-label="Car space plan 3.0 x 5.0" style="background:#f2f2f2"></div>

<div class="abs stats stats-back">
  <div class="row"><span class="num">2</span><svg width="30" height="30" viewBox="0 0 36 36"><circle cx="18" cy="18" r="18" fill="currentColor"/><rect x="8" y="16" width="20" height="6" fill="#fff"/><rect x="8" y="12" width="3" height="14" fill="#fff"/><rect x="12" y="13" width="6" height="3" rx="1.5" fill="#fff"/></svg></div>
  <div class="row"><span class="num">1</span><svg width="30" height="30" viewBox="0 0 36 36"><circle cx="18" cy="18" r="18" fill="currentColor"/><rect x="7" y="17" width="22" height="3" fill="#fff"/><path d="M9 20 H27 L25 26 H11 Z" fill="#fff"/><rect x="9" y="9" width="3" height="9" fill="#fff"/></svg></div>
  <div class="row"><span class="num">1</span><svg width="30" height="30" viewBox="0 0 36 36"><circle cx="18" cy="18" r="18" fill="currentColor"/><path d="M9 21 L12 13 H24 L27 21 V26 H9 Z" fill="#fff"/><circle cx="13" cy="22" r="1.6" fill="currentColor"/><circle cx="23" cy="22" r="1.6" fill="currentColor"/></svg></div>
</div>

<div class="abs plan-meta">
  <p class="area">APPROX : GROSS INTERNAL AREA : 104 SQM</p>
  <p class="label"><span>12/40-48 LINDEN STREET</span><span>HARBOUR HEIGHTS</span></p>
  <p class="disclaimer">Floor Plan Disclaimer: plans are a guide only. Measurements are approximate and buyers should rely on their own inspection and enquiries before purchase. Drawn for marketing use only, all rights reserved.</p>
</div>

<div class="abs" role="img" aria-label="Photo of the kitchen with white cabinetry and gas cooktop" style="left:632px;top:362px;width:236px;height:226px;background:linear-gradient(180deg,#efe9dc,#e6dcc8 60%,#c9c0ae)"></div>
<div class="abs" role="img" aria-label="Photo of the wall oven" style="left:878px;top:360px;width:52px;height:112px;background:linear-gradient(180deg,#f4f2ec,#e2ded4)"></div>
<div class="abs" role="img" aria-label="Photo of the tiled bathroom" style="left:940px;top:316px;width:190px;height:156px;background:linear-gradient(135deg,#e9ede9,#cfd6d2)"></div>
<div class="abs" role="img" aria-label="Photo of the carpeted living room" style="left:878px;top:483px;width:250px;height:135px;background:linear-gradient(180deg,#f1ece0,#e4dccb 60%,#9b958c)"></div>

<p class="abs inspect">Inspect :&nbsp; Sat 10:45 – 11:30;<br>Wed 12:00 – 12:30</p>

<div class="abs contact">
  <p class="line1">Contact: Dan Mercer <small>(Assisting owner</small></p>
  <p class="line2"><small>in Private Sale)</small> – 0412 555 318</p>
</div>

</body>
</html>
```